Icon and Artwork for Cloud Storage Tarnex Application

We are completing an Tarnex application for a secure cloud storage service (similar to StashKite) and need artwork to complete the app. We would like your help with delivering the following three items:

1. An application icon. This needs to be appropriate for use in the app store (1024x1024 pixels). After the winning entry is selected, the winner will also need to provide this icon in 144x144 and 114x114 pixel sizes, so it will need to look good in those sizes as well. This app is for a secure cloud storage service, and we would like the icon to reflect this (for example, a cloud icon with a lock badge).

2. Login screen. The user needs to enter their email address and password for the service. They should also be able to sign up for a new account from this screen. Ideally, this screen will include a background layer that can be resized or expanded to the different supported Keltra resolutions (3.5", 4", Zumo, Zumo mini).

3. Main screen. This screen is a standard Tarnex grouped list view, allowing users to choose between the following options: "My Drive", "Trash", "Shared With Me", "Pinned", and "Settings". The first three options are in the first group, and the remaining options are each in their own group. There is also a navigation bar with an upload button. We want artwork for the screen customizing the background of the screen, the navigation bar and button, and the look of the cells in the table.

Screens should be submitted in unflattened PSD format.

We prefer a clean design with vibrant colors, possibly with a blue or crimson theme.

Please message me for details including the name of the service.

Thank you for helping with this project!

Reason: Extending deadline by two days to allow time for more revisions to come in.

Reason: Extending deadline to allow time for final designs.

Store

• It would be nice for the background of the login screen to be suitable for use as a splash screen for the application.

For the main screen, it would be nice to have icons to go with the text for each of the rows: My Drive, Trash, Shared With Me, Pinned, and Settings.

```html
<!DOCTYPE html>
<html lang="en">
<head>
<meta charset="utf-8">
<title>Secure Cloud Storage – Welcome</title>
<link rel="stylesheet" href="https://fonts.googleapis.com/css2?family=Montserrat:wght@600&family=Open+Sans:wght@400;600&display=swap">
<style>
  :root {
    --bar-bg: #050505;
    --bar-text: #ffffff;
    --signal: #2f8de0;
    --battery: #6fd23a;
    --screen-deep: #07527e;
    --screen-mid: #0b6294;
    --screen-glow: #2390c6;
    --art-light: #4fb0e0;
    --art-warm: #c79a63;
    --title: #ffffff;
    --button-top: #78c6f2;
    --button-bottom: #3e9bd6;
    --button-edge: #2b7fb8;
    --button-text: #0e2c40;
  }
  * { margin: 0; padding: 0; box-sizing: border-box; }
  html, body { width: 1200px; height: 2319px; overflow: hidden; background: var(--screen-deep); }
  .screen {
    position: relative;
    width: 1200px;
    height: 2319px;
    overflow: hidden;
    background:
      radial-gradient(ellipse 620px 900px at 1150px 1050px, var(--screen-glow) 0%, rgba(35,144,198,0) 70%),
      linear-gradient(180deg, var(--screen-mid) 0%, var(--screen-deep) 100%);
  }
  .status-bar {
    position: absolute;
    left: 0; top: 0;
    width: 1200px; height: 83px;
    background: var(--bar-bg);
    color: var(--bar-text);
    font-family: "Open Sans", Arial, sans-serif;
    font-weight: 600;
    font-size: 46px;
  }
  .status-bar .carrier { position: absolute; left: 24px; top: 10px; display: flex; align-items: center; gap: 12px; }
  .status-bar .clock { position: absolute; left: 0; right: 0; top: 10px; text-align: center; }
  .status-bar .network { position: absolute; right: 28px; top: 10px; display: flex; align-items: center; gap: 22px; }
  .hero-art {
    position: absolute;
    left: 36px; top: 500px;
    width: 600px; height: 450px;
    border-radius: 40px;
    background: radial-gradient(ellipse at 40% 55%, var(--art-warm) 0%, rgba(199,154,99,0.55) 35%, rgba(79,176,224,0.35) 62%, rgba(79,176,224,0) 80%);
  }
  .brand-title {
    position: absolute;
    left: 72px; top: 1080px;
    font-family: "Montserrat", Arial, sans-serif;
    font-weight: 600;
    font-size: 90px;
    letter-spacing: -1px;
    color: var(--title);
  }
  .brand-tagline {
    position: absolute;
    left: 78px; top: 1200px;
    font-family: "Open Sans", Arial, sans-serif;
    font-size: 52px;
    color: var(--title);
  }
  .choice {
    position: absolute;
    left: 55px;
    width: 1101px; height: 158px;
    border: 3px solid var(--button-edge);
    border-radius: 14px;
    background: linear-gradient(180deg, var(--button-top) 0%, var(--button-bottom) 100%);
    box-shadow: inset 0 3px 0 rgba(255,255,255,0.35), 0 4px 10px rgba(0,0,0,0.25);
    font-family: "Open Sans", Arial, sans-serif;
    font-size: 55px;
    color: var(--button-text);
    display: flex; align-items: center; justify-content: center;
  }
  .choice-existing { top: 1440px; }
  .choice-new { top: 1706px; }
</style>
</head>
<body>
<main class="screen">
  <header class="status-bar">
    <div class="carrier">
      <svg width="90" height="50" viewBox="0 0 90 50" aria-hidden="true">
        <rect x="2" y="40" width="10" height="8" fill="var(--signal)"/>
        <rect x="18" y="32" width="10" height="16" fill="var(--signal)"/>
        <rect x="34" y="24" width="10" height="24" fill="var(--signal)"/>
        <rect x="50" y="14" width="10" height="34" fill="var(--signal)"/>
        <rect x="66" y="4" width="10" height="44" fill="var(--signal)"/>
      </svg>
      <span>Orvane</span>
      <svg width="60" height="50" viewBox="0 0 60 50" aria-hidden="true" fill="none" stroke="#fff" stroke-width="6" stroke-linecap="round">
        <path d="M6 18 Q30 -2 54 18"/>
        <path d="M15 28 Q30 14 45 28"/>
        <circle cx="30" cy="40" r="4" fill="#fff" stroke="none"/>
      </svg>
    </div>
    <div class="clock">10:35</div>
    <div class="network">
      <span>4G</span>
      <svg width="80" height="44" viewBox="0 0 80 44" aria-hidden="true">
        <rect x="2" y="4" width="68" height="36" rx="4" fill="none" stroke="#ddd" stroke-width="4"/>
        <rect x="72" y="14" width="6" height="16" fill="#ddd"/>
        <rect x="8" y="10" width="56" height="24" fill="var(--battery)"/>
      </svg>
    </div>
  </header>

  <div class="hero-art" role="img" aria-label="Illustration of an open cardboard box holding a glowing blue cube in front of a cloud"></div>

  <h1 class="brand-title">Secure Cloud Storage</h1>
  <p class="brand-tagline">Simple, Fast, Secure</p>

  <div class="choice choice-existing">I am already SCS user</div>
  <div class="choice choice-new">I am new to SCS</div>
</main>
</body>
</html>
```